Book jacket for Drumlore

We need a book jacket design (hard cover front, back, spine, flaps; soft cover and eBook). for a social psychology book with the general cluelessness (being "out of it") of how people function both in their personal and social lives. This is the third book written by the author, a practicing psychiatrist, and the content centers on a single subject, people's lack of genuine emotional contact, their cluelessness with themselves and with current national and world events.

Target Market(s)

People who want to better understand the state the nation and world is in now, and what they can do about it.

Font styles to use
Serif
Sans Serif

Requirements
Must have
• Bold, eye-catching cover
Nice to have
• Like the idea of separating the title word (drum lore) to better emphasize the concept of lack of contact

```html
<!DOCTYPE html>
<html lang="en">
<head>
<meta charset="utf-8">
<title>General Drumloreness – Jacket Concepts</title>
<link rel="stylesheet" href="https://fonts.googleapis.com/css2?family=Montserrat:wght@600;700&family=Poppins:wght@200;300&display=swap">
<style>
  :root {
    --canvas: #efefef;
    --ink-black: #121212;
    --ink-charcoal: #3a3a3a;
    --teal: #2b8fb3;
    --white: #ffffff;
    --sky-dark: #bccde6;
    --sky-light: #e4eefb;
    --violet: #5b62b4;
    --violet-soft: #7a80c6;
    --slate: #56606c;
    --umber-deep: #1f1012;
    --umber-mid: #4a2f2c;
    --skin: #c9a58c;
    --gold: #e9c597;
    --band: rgba(52, 30, 30, 0.78);
  }
  * { box-sizing: border-box; margin: 0; padding: 0; }
  html, body { width: 1200px; height: 1035px; overflow: hidden; }
  body { background: var(--canvas); position: relative; font-family: "Poppins", sans-serif; }

  .cover, .spine { position: absolute; overflow: hidden; }
  .cover { width: 289px; height: 374px; }
  .spine { width: 37px; height: 374px; }

  .title { font-family: "Montserrat", sans-serif; font-weight: 700; text-align: center; line-height: 1.2; }
  .subtitle { font-family: "Poppins", sans-serif; font-weight: 300; text-align: center; text-transform: uppercase; line-height: 1.12; letter-spacing: 0.3px; }
  .author { font-family: "Montserrat", sans-serif; font-weight: 700; text-align: center; text-transform: uppercase; position: absolute; left: 0; right: 0; }
  .artwork { position: absolute; }

  .spine-run {
    position: absolute; left: 0; top: 374px; width: 374px; height: 37px;
    transform-origin: top left; transform: rotate(-90deg);
    display: flex; align-items: center; padding: 0 12px;
  }
  .spine-titles { display: flex; flex-direction: column; gap: 2px; }
  .spine-title { font-family: "Montserrat", sans-serif; font-weight: 700; font-size: 11px; letter-spacing: 0.2px; white-space: nowrap; }
  .spine-subtitle { font-family: "Poppins", sans-serif; font-weight: 300; font-size: 5.6px; white-space: nowrap; text-transform: uppercase; }
  .spine-author { margin-left: auto; align-self: flex-end; margin-bottom: 9px; font-family: "Montserrat", sans-serif; font-weight: 700; font-size: 6.5px; white-space: nowrap; }

  /* Concept one: charcoal */
  .cover--charcoal { left: 73px; top: 75px; background: linear-gradient(90deg, var(--ink-black) 0, var(--ink-black) 16%, #1c1c1c 18%, var(--ink-charcoal) 100%); }
  .cover--charcoal .title { color: var(--teal); font-size: 20.5px; line-height: 1.26; margin-top: 21px; padding-left: 12px; }
  .cover--charcoal .subtitle { color: var(--white); font-size: 14px; margin-top: 26px; padding-left: 12px; }
  .cover--charcoal .artwork {
    left: 70px; top: 180px; width: 165px; height: 138px;
    background: radial-gradient(ellipse closest-side at 62% 50%, #e2e2e2 0, #b8b8b8 35%, rgba(140,140,140,0.55) 65%, rgba(60,60,60,0) 100%);
  }
  .cover--charcoal .author { color: var(--teal); font-size: 11px; top: 343px; padding-left: 12px; }
  .spine--charcoal { left: 477px; top: 75px; background: linear-gradient(90deg, var(--ink-black), #242424); }
  .spine--charcoal .spine-title, .spine--charcoal .spine-subtitle { color: var(--white); }
  .spine--charcoal .spine-author { color: var(--teal); }

  /* Concept two: sky */
  .cover--sky { left: 73px; top: 611px; background: linear-gradient(90deg, var(--sky-dark) 0, #d3e0f2 40%, var(--sky-light) 100%); border-top: 6px solid var(--violet); }
  .cover--sky .title { color: var(--slate); font-size: 23.5px; margin-top: 11px; padding-left: 8px; }
  .cover--sky .subtitle { color: var(--slate); font-size: 14px; margin-top: 9px; }
  .cover--sky .artwork { left: 20px; top: 128px; width: 254px; height: 246px; border-radius: 46% 46% 8px 8px / 40% 40% 8px 8px; background: linear-gradient(135deg, var(--violet) 0, var(--violet-soft) 60%, #8c91d0 100%); }
  .cover--sky .author { color: var(--white); font-size: 7px; top: 353px; }
  .spine--sky { left: 477px; top: 611px; background: linear-gradient(90deg, var(--sky-dark), var(--sky-light)); border-top: 6px solid var(--violet); }
  .spine--sky .spine-title, .spine--sky .spine-subtitle, .spine--sky .spine-author { color: var(--slate); }

  /* Concept three: umber */
  .cover--umber { left: 673px; top: 417px; background: var(--umber-deep); }
  .cover--umber .artwork { inset: 0; background:
      radial-gradient(ellipse at 55% 45%, var(--skin) 0, #9c7866 30%, rgba(74,47,44,0) 62%),
      linear-gradient(180deg, var(--umber-deep) 0, var(--umber-mid) 45%, #8f6d5c 80%, #b89580 100%); }
  .cover--umber .title { position: absolute; left: 0; right: 0; top: 68px; color: var(--white); font-family: "Poppins", sans-serif; font-weight: 300; font-size: 25px; line-height: 1.28; }
  .cover--umber .band { position: absolute; left: 0; right: 0; top: 212px; height: 107px; background: var(--band); }
  .cover--umber .band-base { position: absolute; left: 0; width: 137px; top: 319px; height: 55px; background: var(--umber-deep); }
  .cover--umber .subtitle { position: absolute; left: 0; right: 0; top: 239px; color: var(--white); font-size: 14px; }
  .cover--umber .author { color: var(--gold); font-size: 7px; top: 295px; }
  .spine--umber { left: 1077px; top: 417px; background: linear-gradient(90deg, #140a0b, #2a181a); }
  .spine--umber .spine-title, .spine--umber .spine-subtitle, .spine--umber .spine-author { color: var(--white); }
</style>
</head>
<body>

  <section class="cover cover--charcoal">
    <h1 class="title">GENERAL<br>DRUMLORENESS</h1>
    <p class="subtitle">How people function<br>both in their personal<br>and social lives</p>
    <div class="artwork" role="img" aria-label="Sculpted head profile shattering into fragments"></div>
    <p class="author">Martin B.Hollis</p>
  </section>
  <aside class="spine spine--charcoal">
    <div class="spine-run">
      <div class="spine-titles">
        <span class="spine-title">GENERAL DRUMLORENESS</span>
        <span class="spine-subtitle">How people function both in their personal and social lives</span>
      </div>
      <span class="spine-author">MARTIN B.HOLLIS</span>
    </div>
  </aside>

  <section class="cover cover--sky">
    <h1 class="title">GENERAL<br>DRUMLORENESS</h1>
    <p class="subtitle">How people function<br>both in their personal<br>and social lives</p>
    <div class="artwork" role="img" aria-label="Illustration of two split, fragmented figures in violet tones"></div>
    <p class="author">Martin B.Hollis</p>
  </section>
  <aside class="spine spine--sky">
    <div class="spine-run">
      <div class="spine-titles">
        <span class="spine-title">GENERAL DRUMLORENESS</span>
        <span class="spine-subtitle">How people function both in their personal and social lives</span>
      </div>
      <span class="spine-author">MARTIN B.HOLLIS</span>
    </div>
  </aside>

  <section class="cover cover--umber">
    <div class="artwork" role="img" aria-label="Photograph of a person covering their face with their hands while other hands reach toward them"></div>
    <h1 class="title">GENERAL<br>DRUMLORENESS</h1>
    <div class="band"></div>
    <div class="band-base"></div>
    <p class="subtitle">How people function<br>both in their personal<br>and social lives</p>
    <p class="author">Martin B.Hollis</p>
  </section>
  <aside class="spine spine--umber">
    <div class="spine-run">
      <div class="spine-titles">
        <span class="spine-title">GENERAL DRUMLORENESS</span>
        <span class="spine-subtitle">How people function both in their personal and social lives</span>
      </div>
      <span class="spine-author">MARTIN B.HOLLIS</span>
    </div>
  </aside>

</body>
</html>
```